Website for Nonprofit for kids whose parents have been wounded

We need a web design for a nonprofit that serves children who have been severely burned as well as those whose parents have been wounded during military service. We will be based out of hospitals and will need a format that will encourage trust, safety, and respect. We are stick with a lot of red white and blue. We will also be looking to have a space for donations.

Target Market(s)

Kids and parents of military veterans

Industry/Entity Type

Non Profit

Number of Pages Required

5+ page

Font styles to use
Serif
Decorative

Colors
ec1f27
ffffff
0255a3

Requirements
Must have
• Be both appealing to children and adults. Create a reputable face for our organization. We need an area for donations.
Nice to have
• Something unique

```html
<!DOCTYPE html>
<html lang="en">
<head>
<meta charset="utf-8">
<title>Arc Project — Caring for Children of Wounded Service Members</title>
<link href="https://fonts.googleapis.com/css2?family=Roboto:wght@400;500;700&family=Roboto+Slab:wght@400;700&display=swap" rel="stylesheet">
<style>
:root{
  --blue:#0255a3;
  --blue-light:#2a8ad6;
  --red:#ec1f27;
  --red-soft:#d8414c;
  --white:#ffffff;
  --ink:#333333;
  --muted:#777777;
  --gray-bg:#efefef;
  --line:#dddddd;
  --footer:#2d2d2d;
  --footer-dark:#222222;
  --gold:#f5b400;
}
*{box-sizing:border-box;margin:0;padding:0}
html,body{width:1200px;height:2868px;overflow:hidden}
body{font-family:"Roboto",Arial,sans-serif;color:var(--ink);background:var(--white);font-size:13px;line-height:1.55}
.wrap{width:960px;margin:0 auto;position:relative}
a{color:inherit;text-decoration:none}

/* header */
.site-header{position:absolute;top:0;left:0;width:1200px;height:100px;z-index:5}
.brand{position:absolute;left:32px;top:0;width:216px;height:92px;background:var(--white);display:flex;align-items:center;justify-content:center;box-shadow:0 2px 6px rgba(0,0,0,.15)}
.brand-name{font-family:"Roboto",Arial,sans-serif;font-weight:500;font-size:24px;color:var(--blue)}
.main-nav{position:absolute;left:460px;top:12px;display:flex;gap:26px;font-size:14px;color:var(--white);font-weight:500}
.header-side{position:absolute;right:32px;top:8px;text-align:right;color:var(--white)}
.give-btn{display:inline-block;background:var(--gold);color:var(--blue);font-weight:700;font-size:15px;padding:5px 26px;border-radius:14px;border:1px solid #d99a00}
.header-phone{margin-top:8px;font-size:15px;font-weight:700;display:flex;align-items:center;gap:6px;justify-content:flex-end}

/* hero */
.hero{position:relative;height:580px;overflow:hidden}
.hero-photo{position:absolute;inset:0;background:linear-gradient(100deg,#2f77c6 0%,#4f93d4 38%,#8fb6d6 55%,#7b6a52 72%,#5a4b38 100%)}
.hero-copy{position:absolute;left:128px;top:92px;width:420px;color:var(--white)}
.hero-copy h1{font-size:26px;line-height:34px;font-weight:700}
.btn-start{display:inline-block;margin-top:22px;background:var(--blue-light);color:var(--white);font-weight:500;font-size:15px;padding:11px 22px;border-radius:3px}
.hero-arrow{position:absolute;top:276px;width:22px;height:34px;background:rgba(0,0,0,.45);display:flex;align-items:center;justify-content:center}
.hero-arrow.left{left:0}.hero-arrow.right{right:0}

/* features */
.features{height:320px;padding-top:44px}
.feature-row{display:flex;justify-content:space-between}
.feature{width:220px;text-align:center;border-right:1px solid var(--line);padding:0 18px}
.feature:last-child{border-right:none}
.feature-icon{width:74px;height:74px;border-radius:50%;border:2px solid var(--line);margin:0 auto 16px;display:flex;align-items:center;justify-content:center}
.feature-icon span{width:54px;height:54px;border-radius:50%;display:flex;align-items:center;justify-content:center}
.feature h3{font-size:14px;font-weight:700;margin-bottom:8px;letter-spacing:.5px}
.feature p{font-size:12px;color:var(--muted);line-height:1.5}
.read-more{display:inline-block;margin-top:12px;font-size:12px;font-weight:700;color:var(--red)}

/* about */
.about{height:320px;background:var(--gray-bg);padding-top:34px}
.about .wrap{display:flex;justify-content:space-between}
.section-head{font-family:"Roboto Slab",Georgia,serif;font-size:20px;font-weight:700;color:var(--ink);padding-bottom:6px;border-bottom:2px solid var(--ink);margin-bottom:14px}
.what-we-do{width:700px}
.what-we-do p{font-size:12px;color:var(--muted);margin-bottom:12px;line-height:1.6}
.what-we-do h4{font-size:13px;font-weight:700;margin-bottom:4px}
.inquiry{width:226px}
.inquiry .field{height:30px;background:var(--white);border:1px solid var(--line);margin-bottom:8px;font-size:11px;color:#999;padding:7px 8px}
.inquiry .field.tall{height:54px}
.btn-submit{display:inline-block;background:var(--blue-light);color:var(--white);font-size:12px;font-weight:700;padding:6px 16px;border-radius:2px}

/* programs */
.programs{height:400px;padding-top:32px}
.centered-title{text-align:center;font-family:"Roboto Slab",Georgia,serif;font-size:24px;font-weight:700}
.title-rule{width:340px;height:1px;background:var(--line);margin:10px auto 26px}
.program-row{display:flex;justify-content:space-between}
.program{width:230px;height:270px;position:relative}
.program.featured{background:var(--blue-light);color:var(--white);display:flex;flex-direction:column;align-items:center;justify-content:center;text-align:center}
.program.featured h3{font-family:"Roboto Slab",Georgia,serif;font-size:22px;font-weight:700;line-height:1.2;margin-bottom:16px}
.btn-outline{border:1px solid var(--white);padding:5px 18px;font-size:12px}

/* raise */
.raise{height:320px;position:relative;overflow:hidden}
.raise-bg{position:absolute;inset:0;background:linear-gradient(90deg,#9a9a9a,#cfcfcf 30%,#e6e6e6 50%,#c4c4c4 75%,#8f8f8f)}
.raise-inner{position:relative;text-align:center;padding-top:40px}
.dollar-badge{width:64px;height:64px;border-radius:50%;background:var(--red);color:var(--white);font-size:34px;font-weight:700;line-height:56px;margin:0 auto 12px;border:4px solid var(--white)}
.raise h2{color:var(--red);font-size:38px;font-weight:700;letter-spacing:1px;line-height:1.1;margin-bottom:20px}
.counter{display:flex;justify-content:center;gap:14px}
.counter span{width:48px;height:64px;background:var(--red);color:var(--white);font-size:34px;font-weight:700;line-height:64px;border-radius:3px;box-shadow:0 3px 0 #a3121a}

/* testimonials */
.testimonials{height:380px;padding-top:40px}
.testimonials .sub{text-align:center;font-size:12px;color:var(--muted);margin-top:4px}
.quote-row{display:flex;justify-content:space-between;margin-top:34px}
.quote{width:450px;display:flex;gap:20px}
.quote-person{width:110px;text-align:center;font-size:12px;color:var(--muted)}
.avatar{width:100px;height:100px;border-radius:50%;margin:0 auto 8px}
.quote-body{flex:1;position:relative;padding-left:26px;font-size:12px;color:var(--muted);line-height:1.6}
.quote-mark{position:absolute;left:0;top:-10px;font-family:"Roboto Slab",Georgia,serif;font-size:42px;color:#bbb;line-height:1}
.pager{display:flex;justify-content:center;gap:4px;margin-top:34px}
.pager span{width:20px;height:20px;border:1px solid var(--line);font-size:11px;text-align:center;line-height:18px}
.pager span.on{background:var(--blue-light);color:var(--white);border-color:var(--blue-light)}

/* donate band */
.donate-band{height:110px;background:var(--red-soft);color:var(--white)}
.donate-band .wrap{display:flex;align-items:center;justify-content:space-between;height:110px}
.donate-band p{font-size:20px;font-weight:700;line-height:1.35;width:680px}
.btn-donate{background:var(--blue-light);font-size:22px;font-weight:700;padding:14px 30px;border-radius:3px}

/* footer */
.site-footer{height:438px;background:var(--footer);color:#cfcfcf;position:relative}
.footer-nav{display:flex;justify-content:center;gap:28px;font-size:13px;padding-top:22px;color:var(--white)}
.footer-rule{position:relative;height:1px;background:#555;width:960px;margin:20px auto 0}
.footer-rule i{position:absolute;left:472px;top:-8px;width:16px;height:16px;background:var(--footer);border:1px solid #777;transform:rotate(45deg)}
.footer-cols{display:flex;justify-content:space-between;margin-top:30px}
.footer-col{width:290px}
.footer-col h4{color:var(--white);font-size:13px;font-weight:700;letter-spacing:.5px;padding-bottom:8px;border-bottom:1px solid #555;margin-bottom:14px}
.contact-name{color:var(--blue-light);font-weight:700;margin-bottom:4px}
.contact-line{display:flex;align-items:center;gap:8px;margin-top:10px;font-size:12px}
.map{width:260px;height:150px;background:linear-gradient(135deg,#dfe7dc,#c9d7e6 55%,#e9e3d5)}
.footer-col p{font-size:12px;line-height:1.6}
.news-input{margin-top:14px;height:32px;background:var(--white);color:#999;font-size:11px;padding:8px}
.news-btn{display:inline-block;margin-top:10px;background:var(--blue-light);color:var(--white);font-size:12px;font-weight:700;padding:6px 16px}
.footer-bottom{position:absolute;bottom:0;left:0;width:1200px;height:52px;background:var(--footer-dark)}
.footer-bottom .wrap{display:flex;align-items:center;justify-content:space-between;height:52px;font-size:11px}
.bottom-give{background:var(--gold);color:var(--blue);font-weight:700;font-size:13px;padding:4px 22px;border-radius:12px}
.socials{display:flex;gap:8px}
.socials span{width:24px;height:24px;border-radius:50%;background:#555}
</style>
</head>
<body>

<header class="site-header">
  <a class="brand" href="#"><span class="brand-name">Arc Project</span></a>
  <nav class="main-nav"><a>Home</a><a>About Us</a><a>Projects</a><a>Stories</a><a>Donate</a><a>Contact Us</a></nav>
  <div class="header-side">
    <a class="give-btn">QuickGive</a>
    <div class="header-phone">
      <svg width="14" height="14" viewBox="0 0 24 24"><path fill="#fff" d="M6.6 10.8a15 15 0 0 0 6.6 6.6l2.2-2.2c.3-.3.7-.4 1-.2 1.1.4 2.3.6 3.6.6.6 0 1 .4 1 1V20c0 .6-.4 1-1 1A17 17 0 0 1 3 4c0-.6.4-1 1-1h3.5c.6 0 1 .4 1 1 0 1.3.2 2.5.6 3.6.1.3 0 .7-.2 1z"/></svg>
      (555) 010 7890
    </div>
  </div>
</header>

<section class="hero">
  <div class="hero-photo" role="img" aria-label="Photo of a uniformed service member embracing a child, with a flag in the background"></div>
  <div class="hero-copy">
    <h1>We Serve Children Who Have Been Severely Burned As Well As Those Whose Parents Have Been Wounded During Military Service.</h1>
    <a class="btn-start">GET STARTED WITH US</a>
  </div>
  <span class="hero-arrow left"><svg width="10" height="14" viewBox="0 0 10 14"><path d="M8 1 2 7l6 6" stroke="#fff" stroke-width="2" fill="none"/></svg></span>
  <span class="hero-arrow right"><svg width="10" height="14" viewBox="0 0 10 14"><path d="m2 1 6 6-6 6" stroke="#fff" stroke-width="2" fill="none"/></svg></span>
</section>

<section class="features">
  <div class="wrap feature-row">
    <div class="feature">
      <div class="feature-icon"><span style="background:var(--blue)"><svg width="26" height="26" viewBox="0 0 24 24"><rect x="5" y="4" width="14" height="17" rx="1" fill="none" stroke="#fff" stroke-width="2"/><path d="M8 10h8M8 14h8M8 18h5" stroke="#fff" stroke-width="2"/></svg></span></div>
      <h3>ENROLL</h3>
      <p>Simple steps to register your child for care, camps and family support programs.</p>
      <a class="read-more">Read More</a>
    </div>
    <div class="feature">
      <div class="feature-icon"><span style="background:var(--blue)"><svg width="26" height="26" viewBox="0 0 24 24"><circle cx="12" cy="8" r="4" fill="#fff"/><path d="M4 21c0-4.4 3.6-7 8-7s8 2.6 8 7z" fill="#fff"/></svg></span></div>
      <h3>VOLUNTEER</h3>
      <p>Give your time at partner hospitals and help families feel safe and welcome.</p>
      <a class="read-more">Read More</a>
    </div>
    <div class="feature">
      <div class="feature-icon"><span style="background:var(--red)"><svg width="26" height="26" viewBox="0 0 24 24"><path fill="#fff" d="M12 21 3.5 12.5A5 5 0 0 1 12 5.6a5 5 0 0 1 8.5 6.9z"/></svg></span></div>
      <h3>SUPPORT</h3>
      <p>Every gift funds treatment, counseling and comfort for children in our care.</p>
      <a class="read-more">Read More</a>
    </div>
    <div class="feature">
      <div class="feature-icon"><span style="background:var(--red)"><svg width="26" height="26" viewBox="0 0 24 24"><circle cx="18" cy="5" r="3" fill="#fff"/><circle cx="6" cy="12" r="3" fill="#fff"/><circle cx="18" cy="19" r="3" fill="#fff"/><path d="M6 12 18 5M6 12l12 7" stroke="#fff" stroke-width="2"/></svg></span></div>
      <h3>SHARE</h3>
      <p>Tell friends about our mission and help more families find the help they need.</p>
      <a class="read-more">Read More</a>
    </div>
  </div>
</section>

<section class="about">
  <div class="wrap">
    <div class="what-we-do">
      <h2 class="section-head">What We Do</h2>
      <p>Lorem ipsum dolor sit amet, consectetuer adipiscing elit, sed diam nonummy nibh euismod tincidunt ut laoreet dolore magna aliquam erat volutpat. Ut wisi enim ad minim veniam, quis nostrud exerci tation ullamcorper suscipit lobortis nisl ut aliquip ex ea commodo consequat. Duis autem vel eum iriure dolor in hendrerit in vulputate velit esse molestie consequat, vel illum dolore eu feugiat nulla facilisis at vero eros et accumsan et iusto odio dignissim qui blandit praesent luptatum zzril delenit augue duis dolore te feugait nulla facilisi.</p>
      <h4>Our Mission</h4>
      <p>Lorem ipsum dolor sit amet, consectetuer adipiscing elit, sed diam nonummy nibh euismod tincidunt ut laoreet dolore magna aliquam erat volutpat. Ut wisi enim ad minim veniam.</p>
    </div>
    <div class="inquiry">
      <h2 class="section-head">Quick Inquiry</h2>
      <div class="field">Name</div>
      <div class="field">Email</div>
      <div class="field">Phone</div>
      <div class="field tall">Your message here</div>
      <a class="btn-submit">SUBMIT</a>
    </div>
  </div>
</section>

<section class="programs">
  <h2 class="centered-title">Our Latest Programs</h2>
  <div class="title-rule"></div>
  <div class="wrap program-row">
    <div class="program featured">
      <h3>ADD A SMILE<br>PROGRAM</h3>
      <a class="btn-outline">Read More</a>
    </div>
    <div class="program" role="img" aria-label="Photo of a family sharing a hug at a holiday gathering" style="background:linear-gradient(160deg,#b3463c,#d8b9a0 55%,#7a3a2e)"></div>
    <div class="program" role="img" aria-label="Portrait of a service member in dress uniform" style="background:linear-gradient(180deg,#cfd4d8,#3d4b3e 60%,#2b3528)"></div>
    <div class="program" role="img" aria-label="Photo of a veteran in a wheelchair outdoors" style="background:linear-gradient(180deg,#c9d6e2,#8a9099 55%,#4d5561)"></div>
  </div>
</section>

<section class="raise">
  <div class="raise-bg" role="img" aria-label="Faded photo of children playing"></div>
  <div class="raise-inner">
    <div class="dollar-badge">$</div>
    <h2>YOU'VE HELPED RAISE</h2>
    <div class="counter"><span>5</span><span>1</span><span>3</span><span>5</span><span>5</span><span>8</span><span>3</span></div>
  </div>
</section>

<section class="testimonials">
  <h2 class="centered-title">Words from Our Happy Veterans</h2>
  <p class="sub">See What Say About us</p>
  <div class="wrap quote-row">
    <div class="quote">
      <div class="quote-person"><div class="avatar" role="img" aria-label="Portrait of a veteran" style="background:linear-gradient(160deg,#6c7a5a,#3e4834)"></div>Lorem ipsum</div>
      <div class="quote-body"><span class="quote-mark">&ldquo;</span>Lorem ipsum dolor sit amet, consectetuer adipiscing elit, sed diam nonummy nibh euismod tincidunt ut laoreet dolore magna aliquam erat volutpat. Ut wisi enim ad minim veniam, quis nostrud exerci tation ullamcorper suscipit lobortis nisl ut aliquip ex ea commodo consequat.</div>
    </div>
    <div class="quote">
      <div class="quote-person"><div class="avatar" role="img" aria-label="Portrait of a veteran" style="background:linear-gradient(160deg,#5a7089,#2f3d4c)"></div>Lorem ipsum</div>
      <div class="quote-body"><span class="quote-mark">&ldquo;</span>Lorem ipsum dolor sit amet, consectetuer adipiscing elit, sed diam nonummy nibh euismod tincidunt ut laoreet dolore magna aliquam erat volutpat. Ut wisi enim ad minim veniam, quis nostrud exerci tation ullamcorper suscipit lobortis nisl ut aliquip ex ea commodo consequat.</div>
    </div>
  </div>
  <div class="pager"><span class="on">1</span><span>2</span></div>
</section>

<section class="donate-band">
  <div class="wrap">
    <p>Lorem ipsum dolor sit amet consectetur adipisicing elit sed do eiusmod tempor incididunt ut labore dolor magna aliqua.</p>
    <a class="btn-donate">DONATE NOW</a>
  </div>
</section>

<footer class="site-footer">
  <nav class="footer-nav"><a>Home</a><a>About Us</a><a>Projects</a><a>Stories</a><a>Donate</a><a>Contact Us</a></nav>
  <div class="footer-rule"><i></i></div>
  <div class="wrap footer-cols">
    <div class="footer-col">
      <h4>CONTACT INFORMATION</h4>
      <div class="contact-name">Arc Project Inc.</div>
      <div class="contact-line"><svg width="14" height="14" viewBox="0 0 24 24"><path fill="#cfcfcf" d="M12 2a7 7 0 0 0-7 7c0 5 7 13 7 13s7-8 7-13a7 7 0 0 0-7-7zm0 9.5A2.5 2.5 0 1 1 12 6.5a2.5 2.5 0 0 1 0 5z"/></svg><span>Street Name City Name<br>State, Zipcode</span></div>
      <div class="contact-line"><svg width="14" height="14" viewBox="0 0 24 24"><path fill="#cfcfcf" d="M6.6 10.8a15 15 0 0 0 6.6 6.6l2.2-2.2c.3-.3.7-.4 1-.2 1.1.4 2.3.6 3.6.6.6 0 1 .4 1 1V20c0 .6-.4 1-1 1A17 17 0 0 1 3 4c0-.6.4-1 1-1h3.5c.6 0 1 .4 1 1 0 1.3.2 2.5.6 3.6.1.3 0 .7-.2 1z"/></svg>(555) 010 7890</div>
      <div class="contact-line"><svg width="14" height="14" viewBox="0 0 24 24"><rect x="2" y="5" width="20" height="14" rx="1" fill="#cfcfcf"/><path d="m2 6 10 7 10-7" stroke="#2d2d2d" stroke-width="2" fill="none"/></svg>hello@arcproject.org</div>
    </div>
    <div class="footer-col">
      <h4>LOCATION MAP</h4>
      <div class="map" role="img" aria-label="Street map showing the office location"></div>
    </div>
    <div class="footer-col">
      <h4>NEWSLETTER SIGNUP</h4>
      <p>Lorem ipsum dolor sit amet, consectetuer adipiscing elit, sed diam nonummy nibh euismod tincidunt ut laoreet dolore.</p>
      <div class="news-input">Enter your email here</div>
      <a class="news-btn">SUBMIT</a>
    </div>
  </div>
  <div class="footer-bottom">
    <div class="wrap">
      <span>Copyright &copy; 2014 Arc Project Inc. All rights reserved.</span>
      <a class="bottom-give">QuickGive</a>
      <div class="socials"><span></span><span></span><span></span><span></span></div>
    </div>
  </div>
</footer>

</body>
</html>
```